Label for high-end indie coffee package

I need a label for high-end indie coffee package.

Coffee comes from Mt. Elgon, Trans-Nzoia County, Kenya. The coffee will be sold in Finland. The package as such will be semi matte black and the label will be printed out as a sticker.

Maximum measurements for the label would around 9 x 9 centimeters. It can be a square / rectangle / circle. I would like it to include influences from coffee origins (Kenya) and also demonstrate the high-end quality of the coffee with the modern twist.

The label should include the following text:

Coffee Name:
Morelu Vintaro AA
Washed & Natural

Origins:
Mt. Elgon, Trans-Nzoia County, Kenya

Growing altitude:
Altitude: 1 800 amsl

Coffee variety:
100 % Arabica

Following fields should be possible to be filled afterwards when the need occurs:
roast date
best before
roasted by

I'll be more than happy to answer any questions!

Finland. High-end customers, design coffee shops.

```html
<!DOCTYPE html>
<html lang="en">
<head>
<meta charset="utf-8">
<title>Morelu Vintaro AA – Coffee Label Options</title>
<link rel="stylesheet" href="https://fonts.googleapis.com/css2?family=Great+Vibes&family=Hind:wght@600&family=Marcellus&family=Tinos&display=swap">
<style>
  :root {
    --sheet: #ffffff;
    --ink: #000000;
    --label-black: #000000;
    --text-light: #ffffff;
    --gold: #e2a93b;
    --gold-light: #f8dd85;
    --gold-deep: #c28b3e;
    --bean-brown: #5a4226;
  }
  html, body {
    margin: 0;
    padding: 0;
    width: 1200px;
    height: 717px;
    overflow: hidden;
    background: var(--sheet);
  }
  .presentation-board {
    display: block;
    width: 1200px;
    height: 717px;
  }
  .board-edge { fill: var(--sheet); stroke: var(--ink); stroke-width: 3; }
  .panel-edge { fill: var(--sheet); stroke: var(--ink); stroke-width: 2; }
  .label-body { fill: var(--label-black); }
  .gold-frame { fill: none; stroke: url(#goldSheen); stroke-width: 19; stroke-linejoin: miter; }
  .info-text {
    font-family: "Tinos", "Times New Roman", serif;
    font-size: 22px;
    fill: var(--text-light);
    text-anchor: middle;
  }
  .info-text.left { text-anchor: start; }
  .name-caps {
    font-family: "Marcellus", serif;
    font-size: 60px;
    fill: url(#goldSheen);
    text-anchor: middle;
  }
  .name-script {
    font-family: "Great Vibes", cursive;
    font-size: 82px;
    fill: url(#goldSheen);
    text-anchor: middle;
  }
  .process-line {
    font-family: "Hind", sans-serif;
    font-weight: 600;
    font-size: 48px;
    fill: var(--text-light);
    text-anchor: middle;
  }
  .tick-box { fill: none; stroke: var(--text-light); stroke-width: 3; }
</style>
</head>
<body>
<svg class="presentation-board" viewBox="0 0 2362 1411" xmlns="http://www.w3.org/2000/svg">
  <defs>
    <linearGradient id="goldSheen" x1="0" y1="0" x2="1" y2="0">
      <stop offset="0" stop-color="var(--gold)"/>
      <stop offset="0.55" stop-color="var(--gold-light)"/>
      <stop offset="1" stop-color="var(--gold-deep)"/>
    </linearGradient>
    <linearGradient id="beanFadeDown" x1="0" y1="0" x2="0" y2="1">
      <stop offset="0" stop-color="var(--bean-brown)"/>
      <stop offset="1" stop-color="var(--label-black)"/>
    </linearGradient>
    <linearGradient id="beanFadeUp" x1="0" y1="1" x2="0" y2="0">
      <stop offset="0" stop-color="var(--bean-brown)"/>
      <stop offset="1" stop-color="var(--label-black)"/>
    </linearGradient>
    <linearGradient id="beanFadeRight" x1="0" y1="0" x2="1" y2="0">
      <stop offset="0" stop-color="var(--bean-brown)"/>
      <stop offset="1" stop-color="var(--label-black)"/>
    </linearGradient>
    <linearGradient id="beanFadeLeft" x1="1" y1="0" x2="0" y2="0">
      <stop offset="0" stop-color="var(--bean-brown)"/>
      <stop offset="1" stop-color="var(--label-black)"/>
    </linearGradient>
    <linearGradient id="bronzeWash" x1="0" y1="0" x2="0" y2="1">
      <stop offset="0" stop-color="var(--label-black)"/>
      <stop offset="1" stop-color="#bb8c42"/>
    </linearGradient>

    <g id="labelShape">
      <path class="label-body" d="M322 154 H909 V408 L1004 462 V912 L909 966 V1217 H322 V966 L227 912 V462 L322 408 Z"/>
    </g>
    <g id="labelFrame">
      <path class="gold-frame" d="M350 181 H881 V420 L976 473 V893 L615 1100 L254 893 V473 L350 420 Z"/>
      <path class="gold-frame" d="M350 975 V1192 H881 V975"/>
    </g>
    <g id="labelDetails">
      <text class="info-text" x="615" y="401">Origins:</text>
      <text class="info-text" x="615" y="428">Mt. Elgon, Trans-Nzoia County, Kenya</text>
      <text class="process-line" x="615" y="598">Washed &amp; Natural</text>
      <text class="info-text" x="615" y="677">COFFEE VARIETY:</text>
      <rect class="tick-box" x="511" y="734" width="33" height="33"/>
      <rect class="tick-box" x="511" y="788" width="33" height="33"/>
      <rect class="tick-box" x="511" y="842" width="33" height="33"/>
      <rect class="tick-box" x="511" y="896" width="33" height="33"/>
      <rect class="tick-box" x="511" y="950" width="33" height="33"/>
      <text class="info-text left" x="574" y="759">100 % Arabica</text>
      <text class="info-text left" x="574" y="813">........................</text>
      <text class="info-text left" x="574" y="867">........................</text>
      <text class="info-text left" x="574" y="921">........................</text>
      <text class="info-text left" x="574" y="975">........................</text>
      <text class="info-text" x="615" y="1138">Growing altitude:</text>
      <text class="info-text" x="615" y="1165">Altitude: 1 800 amsl</text>
    </g>
  </defs>

  <rect class="board-edge" x="1.5" y="1.5" width="2359" height="1408"/>

  <!-- Option one: caps name, bronze wash -->
  <g class="label-option label-option--caps">
    <rect class="panel-edge" x="84" y="154" width="1063" height="1063"/>
    <use href="#labelShape"/>
    <rect role="img" aria-label="Coffee bean pattern fading into black" x="322" y="154" width="587" height="250" fill="url(#beanFadeDown)"/>
    <rect role="img" aria-label="Coffee bean pattern fading into black" x="322" y="970" width="587" height="247" fill="url(#beanFadeUp)"/>
    <polygon points="341,685 890,685 890,912 615,1070 341,912" fill="url(#bronzeWash)"/>
    <use href="#labelFrame"/>
    <text class="name-caps" x="615" y="546">MORELU VINTARO AA</text>
    <use href="#labelDetails"/>
  </g>

  <!-- Option two: script name, side bean wings -->
  <g class="label-option label-option--script" transform="translate(1129 -5)">
    <rect class="panel-edge" x="84" y="154" width="1063" height="1063"/>
    <use href="#labelShape"/>
    <polygon role="img" aria-label="Coffee bean pattern on left wing" points="227,440 420,440 420,990 227,912" fill="url(#beanFadeRight)"/>
    <polygon role="img" aria-label="Coffee bean pattern on right wing" points="810,440 1004,440 1004,912 810,990" fill="url(#beanFadeLeft)"/>
    <rect role="img" aria-label="Coffee bean pattern on upper edges" x="322" y="154" width="70" height="260" fill="url(#beanFadeRight)"/>
    <rect role="img" aria-label="Coffee bean pattern on upper edges" x="839" y="154" width="70" height="260" fill="url(#beanFadeLeft)"/>
    <use href="#labelFrame"/>
    <text class="name-script" x="615" y="542">Morelu Vintaro AA</text>
    <use href="#labelDetails"/>
  </g>
</svg>
</body>
</html>
```